Business Card - Tally Forge

Need Business Card design for company named Tally Forge. Software development focused mainly on Brindle Kelvox & Vuro Apps. I've attached our logo with both a black and white background. Please add trademark symbol to logo when using.

```html
<!DOCTYPE html>
<html lang="en">
<head>
<meta charset="utf-8">
<title>Tally Forge – Business Card</title>
<link rel="stylesheet" href="https://fonts.googleapis.com/css2?family=Exo+2:wght@500;600&display=swap">
<style>
  :root {
    --backdrop: #e8e8e8;
    --card: #ffffff;
    --ink: #3a3a3a;
    --brand-yellow: #f9c21a;
    --brand-orange: #f08a24;
    --brand-red: #d82027;
    --on-red: #ffffff;
  }
  * { box-sizing: border-box; margin: 0; padding: 0; }
  html, body {
    width: 1200px;
    height: 948px;
    overflow: hidden;
    background: var(--backdrop);
    font-family: "Exo 2", sans-serif;
  }
  .stage {
    position: relative;
    width: 1200px;
    height: 948px;
  }
  .card {
    position: absolute;
    top: 207px;
    width: 287px;
    height: 502px;
    background: var(--card);
    overflow: hidden;
    box-shadow: 0 2px 8px rgba(0, 0, 0, 0.18);
  }
  .card--front { left: 273px; }
  .card--back { left: 630px; }

  .brand-band {
    position: absolute;
    left: 20px;
    top: 45px;
    width: 300px;
    height: 286px;
    border-radius: 26px 0 0 26px;
    background: linear-gradient(90deg, var(--brand-yellow) 0%, var(--brand-orange) 50%, var(--brand-red) 100%);
  }

  .contact-panel {
    position: absolute;
    left: 0;
    top: 45px;
    width: 251px;
    height: 286px;
    border-radius: 0 26px 26px 0;
    background: var(--brand-red);
    color: var(--on-red);
    padding: 106px 0 0 27px;
    font-size: 12.5px;
    font-weight: 500;
    line-height: 1.18;
  }
  .contact-panel address { font-style: normal; margin-bottom: 15px; }
  .contact-panel .label { margin-left: 6px; }

  .wordmark {
    position: absolute;
    left: 0;
    right: 0;
    top: 598px;
    top: 391px;
    text-align: center;
    color: var(--ink);
    font-size: 38px;
    font-weight: 600;
    letter-spacing: -1.5px;
    line-height: 1;
  }
  .wordmark sup {
    font-size: 9px;
    letter-spacing: 0;
    vertical-align: top;
    position: relative;
    top: 2px;
    margin-left: 2px;
  }
</style>
</head>
<body>
<main class="stage">
  <section class="card card--front">
    <div class="brand-band" role="img" aria-label="Brand colour band in yellow, orange and red"></div>
    <p class="wordmark">Tally Forge<sup>TM</sup></p>
  </section>

  <section class="card card--back">
    <div class="contact-panel">
      <address>2240 Harbor Row<br>Dunmore, FL 33990</address>
      <p>555-014-2290<span class="label">Mobile</span></p>
      <p>555-014-7731<span class="label">Fax</span></p>
    </div>
    <p class="wordmark">Tally Forge<sup>TM</sup></p>
  </section>
</main>
</body>
</html>
```